Book Cover Design 'Boundless Tide - Lessons In Inner Sovereignty'

I need to see pitches / artwork for a book cover for new book designed to start a new global spiritual movement and save humanity. The book merges science and spirituality and explains to the reader why they are an all powerful god.

```html
<!DOCTYPE html>
<html lang="en">
<head>
<meta charset="utf-8">
<title>Boundless Tide – Lessons In Inner Sovereignty</title>
<link rel="stylesheet" href="https://fonts.googleapis.com/css2?family=Bodoni+Moda:opsz,wght@6..96,700;6..96,800&family=Playfair+Display:wght@700&display=swap">
<style>
  :root {
    --navy-core: #1c2250;
    --navy-mid: #141a44;
    --navy-edge: #0a0d2a;
    --pink-hot: #ff2f9e;
    --pink-light: #ff9ad6;
    --pink-deep: #d81b85;
    --white: #ffffff;
  }
  html, body {
    margin: 0;
    padding: 0;
    width: 800px;
    height: 1200px;
    overflow: hidden;
    background: var(--navy-edge);
  }
  .cover {
    position: relative;
    width: 800px;
    height: 1200px;
    overflow: hidden;
    background: radial-gradient(ellipse 70% 60% at 50% 45%, var(--navy-core) 0%, var(--navy-mid) 45%, var(--navy-edge) 100%);
  }
  .cover-art {
    position: absolute;
    inset: 0;
    width: 800px;
    height: 1200px;
    display: block;
  }
  .title-text {
    font-family: "Bodoni Moda", "Playfair Display", serif;
    font-weight: 700;
  }
  .title-fill { fill: url(#pinkSheen); }
  .title-edge { fill: var(--white); opacity: 0.75; }
  .title-rule { stroke: var(--pink-hot); stroke-width: 4; }
  .author-rule { stroke: var(--white); stroke-width: 3; }
  .author-name {
    font-family: "Playfair Display", serif;
    font-weight: 700;
    fill: var(--white);
    letter-spacing: 3px;
  }
</style>
</head>
<body>
  <main class="cover">
    <svg class="cover-art" viewBox="0 0 800 1200" xmlns="http://www.w3.org/2000/svg">
      <defs>
        <linearGradient id="pinkSheen" x1="0" y1="0" x2="0" y2="1">
          <stop offset="0" stop-color="#ff9ad6"/>
          <stop offset="0.35" stop-color="#ff2f9e"/>
          <stop offset="0.55" stop-color="#d81b85"/>
          <stop offset="0.75" stop-color="#ff2f9e"/>
          <stop offset="1" stop-color="#ff9ad6"/>
        </linearGradient>
      </defs>

      <g class="title" role="heading" aria-level="1" aria-label="Boundless Tide – Lessons In Inner Sovereignty">
        <!-- Line: BOUNDLESS -->
        <text class="title-text title-edge" x="402" y="242" font-size="115" text-anchor="middle" textLength="640" lengthAdjust="spacingAndGlyphs">BOUNDLESS</text>
        <text class="title-text title-fill" x="400" y="240" font-size="115" text-anchor="middle" textLength="640" lengthAdjust="spacingAndGlyphs">BOUNDLESS</text>

        <!-- Line: TIDE -->
        <text class="title-text title-edge" x="402" y="422" font-size="190" text-anchor="middle" textLength="520" lengthAdjust="spacingAndGlyphs">TIDE</text>
        <text class="title-text title-fill" x="400" y="420" font-size="190" text-anchor="middle" textLength="520" lengthAdjust="spacingAndGlyphs">TIDE</text>

        <!-- Joiner row: LESSONS IN -->
        <line class="title-rule" x1="110" y1="483" x2="205" y2="483"/>
        <line class="title-rule" x1="595" y1="483" x2="690" y2="483"/>
        <text class="title-text title-edge" x="401" y="502" font-size="54" text-anchor="middle" textLength="360" lengthAdjust="spacingAndGlyphs">LESSONS IN</text>
        <text class="title-text title-fill" x="400" y="501" font-size="54" text-anchor="middle" textLength="360" lengthAdjust="spacingAndGlyphs">LESSONS IN</text>

        <!-- Line: INNER -->
        <text class="title-text title-edge" x="402" y="692" font-size="170" text-anchor="middle" textLength="560" lengthAdjust="spacingAndGlyphs">INNER</text>
        <text class="title-text title-fill" x="400" y="690" font-size="170" text-anchor="middle" textLength="560" lengthAdjust="spacingAndGlyphs">INNER</text>

        <!-- Line: SOVEREIGNTY -->
        <text class="title-text title-edge" x="402" y="842" font-size="100" text-anchor="middle" textLength="640" lengthAdjust="spacingAndGlyphs">SOVEREIGNTY</text>
        <text class="title-text title-fill" x="400" y="840" font-size="100" text-anchor="middle" textLength="640" lengthAdjust="spacingAndGlyphs">SOVEREIGNTY</text>
      </g>

      <g class="author-block">
        <line class="author-rule" x1="170" y1="940" x2="630" y2="940"/>
        <line class="author-rule" x1="170" y1="1074" x2="630" y2="1074"/>
        <text class="author-name" x="400" y="1022" font-size="40" text-anchor="middle" textLength="430" lengthAdjust="spacingAndGlyphs">MARCUS ELLERY VANE</text>
      </g>
    </svg>
  </main>
</body>
</html>
```